Need A Homepage Redesign For Ecommerce Store

Just looking for a great quality designer to redesign my homepage. We will take current structure and redesign to make it cleaner and more user friendly.

Our website is here - www.purelumenfilters.com

Please see the attached for the layout structure that we would like. Please be creative as well.

As you can see the current design does not look clean and is not user friendly.

See attached and thank you and good luck!

P.S. Whoever wins I will give them the next work for product pages and other landing pages.

Target Market(s)

Middle to upper class health minded people, ages 30 and up

Industry/Entity Type

Health And Wellness

Number of Pages Required

1 page

Font styles to use
Sans Serif

Colors
0255a3
0792cd
00a990

Requirements
Must have
• Clean design. Professional design. Use current logo and tagline (unless you think you can do better).
Nice to have
• I would like to see some creativity as well.
Should not have
• Please dont use the same structure as I have. Want this to be a total redesign.

```html
<!DOCTYPE html>
<html lang="en">
<head>
<meta charset="utf-8">
<title>PureLumen Water Ionizers</title>
<link href="https://fonts.googleapis.com/css2?family=Open+Sans:wght@400;600;700&family=Oswald:wght@300;400&family=Quicksand:wght@400;500&display=swap" rel="stylesheet">
<style>
:root{
  --blue:#2aa3de;
  --blue-dark:#1e8fc7;
  --ink:#3a4147;
  --text:#444a50;
  --muted:#8a9096;
  --teal:#4ecfdc;
  --sun:#f2d06b;
  --coral:#ec5b62;
  --panel:#eeeff1;
  --white:#ffffff;
  --line:#dfe2e5;
}
*{box-sizing:border-box;margin:0;padding:0}
html,body{width:1200px;height:2317px;overflow:hidden;background:var(--white)}
body{position:relative;font-family:"Open Sans",Arial,sans-serif;color:var(--text)}
.abs{position:absolute}
.topbar{left:0;top:0;width:1200px;height:28px;background:var(--blue)}
.topbar .account{position:absolute;right:112px;top:6px;color:#fff;font-size:11px;display:flex;gap:6px;align-items:center}
.topbar .social{position:absolute;right:28px;top:0;display:flex}
.topbar .social span{width:33px;height:28px;display:block}
.social .s1{background:#35558f}.social .s2{background:#d9443a}
.brand{left:156px;top:47px;display:flex;align-items:center;gap:10px}
.brand .mark{width:40px;height:40px;border-radius:50%;background:var(--blue)}
.brand .name{font-size:16px;font-weight:700;color:var(--blue);letter-spacing:.4px;line-height:1}
.brand .tag{font-size:8px;font-weight:700;color:var(--blue);letter-spacing:.6px;margin-top:4px}
.search{left:535px;top:53px;width:232px;height:31px;border:1px solid #cfd3d7;border-radius:16px;font-size:10px;color:var(--muted);padding:9px 14px}
.search svg{position:absolute;right:12px;top:8px}
.phone{left:812px;top:56px;font-family:"Oswald",sans-serif;font-size:19px;color:var(--ink);display:flex;gap:8px;align-items:center}
.cart{left:1004px;top:53px;width:32px;height:32px;border:2px solid var(--blue);border-radius:50%}
.cart .count{position:absolute;right:-7px;top:-7px;width:15px;height:15px;border-radius:50%;background:var(--ink);color:#fff;font-size:7px;text-align:center;line-height:15px}
.nav{left:0;top:108px;width:1200px;height:36px;background:var(--ink)}
.nav ul{list-style:none;display:flex;position:absolute;left:156px;top:0;height:36px}
.nav li{color:#e7eaec;font-size:12px;line-height:36px;padding:0 16px}
.nav li.home{background:transparent;border-bottom:3px solid var(--blue);padding:0 19px}
.hero{left:156px;top:159px;width:888px;height:400px;background:linear-gradient(135deg,#4a4f6f 0%,#6e6f8e 35%,#9ea3b8 60%,#5e6c84 100%);overflow:hidden}
.hero .product{position:absolute;left:110px;top:60px;width:300px;height:250px;background:linear-gradient(160deg,#f2f3f5,#c9ccd2);border-radius:8px;opacity:.9}
.hero .copy{position:absolute;left:432px;top:96px;width:360px;text-align:center;color:#fff}
.hero .script{position:absolute;left:110px;top:-40px;width:140px;height:46px;background:rgba(42,163,222,.55);border-radius:20px}
.hero h2{font-size:21px;font-weight:600;position:relative}
.hero .off{font-family:"Oswald",sans-serif;font-weight:300;font-size:38px;color:#f5e646;margin-top:16px;line-height:1}
.hero .lead{font-size:14px;margin-top:8px}
.hero .brandline{font-size:20px;font-weight:600;letter-spacing:.5px}
.coupon{display:inline-flex;margin-top:10px;align-items:stretch}
.coupon .lbl{border:1px dashed #fff;font-size:11px;padding:5px 10px}
.coupon .code{background:#e8262c;font-family:"Oswald",sans-serif;font-size:15px;padding:2px 8px}
.btn-dark{display:inline-block;background:var(--ink);color:#fff;font-size:11px;font-weight:600;padding:8px 26px}
.hero .btn-dark{margin-top:38px;padding:9px 26px}
.arrow{position:absolute;width:28px;height:56px}
.hero .arrow.l{left:0;top:172px}
.hero .arrow.r{right:0;top:172px}
.perks{left:156px;top:576px;width:888px;height:56px;display:flex}
.perks div{flex:1;display:flex;align-items:center;justify-content:center;gap:8px;color:#fff;font-size:14px;font-weight:600}
.perks .p1{background:var(--teal)}
.perks .p2{background:var(--sun);color:var(--ink);border:2px solid #e3bc4e}
.perks .p3{background:var(--coral)}
.products{left:156px;top:660px;width:888px;display:flex}
.card{flex:1;text-align:center}
.card .shot{width:210px;height:210px;margin:0 auto;border-radius:50%;background:radial-gradient(circle,#e7f3fb 0%,#bfe0f3 55%,#ffffff 72%)}
.card h3{font-size:16px;font-weight:400;color:var(--blue);margin-top:20px}
.card p{font-size:14px;margin-top:2px}
.card .btn-dark{margin-top:16px;padding:8px 26px}
.card .btn-blue{background:var(--blue)}
.stories{left:0;top:1030px;width:1200px;height:398px;background:linear-gradient(120deg,#4f5a3a 0%,#8a7a5c 35%,#6b5f4e 60%,#3b3a36 100%)}
.stories .quote-bg{position:absolute;left:611px;top:0;width:589px;height:398px;background:rgba(40,42,48,.72)}
.help{position:absolute;left:156px;top:138px;color:#fff}
.help h2{font-family:"Quicksand",sans-serif;font-weight:400;font-size:27px}
.help h3{font-size:16px;font-weight:600;margin-top:4px;letter-spacing:.3px}
.help .links{display:flex;gap:15px;margin-top:24px}
.outline{border:1px solid #fff;font-size:11px;font-weight:600;padding:8px 19px}
.quote{position:absolute;left:687px;top:52px;width:270px;color:#fff;font-size:13px;line-height:20px}
.quote .mark{font-size:26px;font-family:Georgia,serif;line-height:20px}
.quote .rule{width:280px;height:1px;background:rgba(255,255,255,.35);margin-top:72px}
.quote .who{color:var(--blue);font-size:18px;margin-top:24px}
.quote .where{color:var(--blue);font-size:13px;margin-top:4px}
.confidence{left:0;top:1480px;width:1200px;text-align:center}
.confidence h2{font-family:"Quicksand",sans-serif;font-weight:500;font-size:28px;color:var(--ink)}
.confidence .sub{font-family:"Quicksand",sans-serif;font-size:16px;color:var(--muted);margin-top:0}
.pillars{position:absolute;left:156px;top:98px;width:888px;display:flex}
.pillar{flex:1;text-align:center}
.pillar .ring{width:96px;height:96px;border-radius:50%;border:2px solid var(--blue);margin:0 auto;display:flex;align-items:center;justify-content:center}
.pillar .ring.fill{background:var(--blue)}
.pillar h4{font-size:14px;font-weight:600;color:var(--ink);margin-top:30px;letter-spacing:.3px}
.pillar p{font-size:12px;color:var(--muted);line-height:16px;margin-top:6px}
.contact{left:0;top:1803px;width:1200px;height:385px;background:var(--panel);text-align:center}
.contact h2{font-family:"Quicksand",sans-serif;font-weight:500;font-size:28px;color:var(--ink);margin-top:52px}
.contact .sub{font-size:13px;color:var(--muted);margin-top:4px}
.form{position:absolute;left:236px;top:136px;width:728px}
.row{display:flex;gap:18px}
.field{flex:1;height:30px;background:#fff;border:1px solid var(--line);font-size:11px;color:var(--muted);text-align:left;padding:8px 12px}
.area{height:94px;margin-top:18px;flex:none;width:100%}
.send{margin-top:17px;height:31px;background:var(--blue);color:#fff;font-size:12px;font-weight:600;line-height:31px;border:1px solid var(--blue-dark)}
.footer{left:0;top:2188px;width:1200px;height:129px;background:var(--ink)}
.footer .links{position:absolute;left:156px;top:48px;font-size:13px;color:#aab0b5}
.footer .links b{font-weight:400;color:var(--blue)}
.footer .copy{position:absolute;left:156px;top:70px;font-size:11px;color:#9aa0a5}
.footer .social{position:absolute;left:919px;top:51px;display:flex}
.footer .social span{width:30px;height:28px;display:block}
.footer .social .s1{background:#fff}
.footer .up{position:absolute;left:1013px;top:52px;width:31px;height:28px;background:var(--blue);display:flex;align-items:center;justify-content:center}
</style>
</head>
<body>

<div class="abs topbar">
  <div class="account">
    <svg width="12" height="12" viewBox="0 0 12 12"><circle cx="6" cy="4" r="2.6" fill="none" stroke="#fff"/><path d="M1 12c0-3 2.3-4.5 5-4.5s5 1.5 5 4.5" fill="none" stroke="#fff"/></svg>
    Login / Register
  </div>
  <div class="social"><span class="s1"></span><span class="s2"></span></div>
</div>

<div class="abs brand">
  <div class="mark"></div>
  <div>
    <div class="name">PUREELUMEN WATER IONIZERS</div>
    <div class="tag">RIDE THE WAVE TO A HEALTHIER YOU!</div>
  </div>
</div>

<div class="abs search">Search here ...
  <svg width="13" height="13" viewBox="0 0 13 13"><circle cx="5.5" cy="5.5" r="4" fill="none" stroke="#2aa3de" stroke-width="2"/><path d="M8.5 8.5l3.5 3.5" stroke="#2aa3de" stroke-width="2"/></svg>
</div>

<div class="abs phone">
  <svg width="20" height="20" viewBox="0 0 20 20"><circle cx="10" cy="10" r="8.5" fill="none" stroke="#3a4147" stroke-width="1.5"/><path d="M7 5.5l2 2-1 1.5c.7 1.5 1.6 2.4 3 3l1.5-1 2 2-1.5 1.5C9.5 14 6 10.5 5.5 7z" fill="#3a4147"/></svg>
  888 - 555 0142
</div>

<div class="abs cart">
  <svg width="28" height="28" viewBox="0 0 28 28"><path d="M8 10h2l1.5 7h7l1.5-5H11" fill="none" stroke="#2aa3de" stroke-width="1.6"/><circle cx="12.5" cy="19.5" r="1" fill="#2aa3de"/><circle cx="17.5" cy="19.5" r="1" fill="#2aa3de"/></svg>
  <span class="count">02</span>
</div>

<nav class="abs nav">
  <ul>
    <li class="home"><svg width="12" height="11" viewBox="0 0 12 11"><path d="M6 0L0 5.5h1.6V11h3.2V7.5h2.4V11h3.2V5.5H12z" fill="#2aa3de"/></svg></li>
    <li>Browse Products</li>
    <li>Why PureLumen?</li>
    <li>Compare</li>
    <li>Support</li>
    <li>Water Ionizer Info</li>
    <li>Testimonials</li>
    <li>Contact Us</li>
  </ul>
</nav>

<section class="abs hero" role="img" aria-label="Summer sale banner with a faceted violet background and two countertop water ionizers">
  <div class="product" role="img" aria-label="Two white water ionizer units with spout"></div>
  <div class="copy">
    <div class="script" role="img" aria-label="Hand-lettered word Super"></div>
    <h2>Summer Sale Going On Now</h2>
    <div class="off">20% off</div>
    <div class="lead">Start Enjoying the Power of</div>
    <div class="brandline">PURELUMEN</div>
    <div class="coupon"><span class="lbl">Use Coupon Code</span><span class="code">200ff</span></div><br>
    <span class="btn-dark">Shop Now</span>
  </div>
  <svg class="arrow l" viewBox="0 0 28 56"><path d="M0 0l28 28L0 56z" fill="#fff"/><path d="M12 23l-5 5 5 5" fill="none" stroke="#2aa3de" stroke-width="2.5"/></svg>
  <svg class="arrow r" viewBox="0 0 28 56"><path d="M28 0L0 28l28 28z" fill="#2aa3de"/><path d="M16 23l5 5-5 5" fill="none" stroke="#fff" stroke-width="2.5"/></svg>
</section>

<div class="abs perks">
  <div class="p1"><svg width="13" height="15" viewBox="0 0 13 15"><path d="M6.5 0L0 2.5v4.5c0 4 3 7 6.5 8 3.5-1 6.5-4 6.5-8V2.5z" fill="#fff"/></svg>Lifetime Warranty</div>
  <div class="p2"><svg width="15" height="15" viewBox="0 0 15 15"><path d="M14 1l-5 4.5-6-1.5-1.5 1.5 4.5 3-2.5 2.5-2-.5L0 11.5l3 1 1 3 1-1.5-.5-2 2.5-2.5 3 4.5 1.5-1.5-1.5-6L15 2z" fill="#3a4147"/></svg>Free Shipping</div>
  <div class="p3"><span style="font-size:17px">$</span>100% Money Back Guarantee</div>
</div>

<div class="abs products">
  <div class="card">
    <div class="shot" role="img" aria-label="White water ionizer with water splash"></div>
    <h3>Our Best Seller!</h3>
    <p>PureLumen Crest Plus Ionizer</p>
    <span class="btn-dark">Shop Now</span>
  </div>
  <div class="card">
    <div class="shot" role="img" aria-label="Black water ionizer with water splash"></div>
    <h3>Perfect "In-Between Machine</h3>
    <p>PureLumen Harbor Ionizer</p>
    <span class="btn-dark btn-blue">Shop Now</span>
  </div>
  <div class="card">
    <div class="shot" role="img" aria-label="Silver water ionizer with water splash"></div>
    <h3>Our Super Saver!</h3>
    <p>PureLumen Breaker Ionizer</p>
    <span class="btn-dark">Shop Now</span>
  </div>
</div>

<section class="abs stories" role="img" aria-label="Outdoor photo of a smiling mother and daughter with a father in the background">
  <div class="quote-bg"></div>
  <div class="help">
    <h2>Still Need Help?</h2>
    <h3>Decide to Right Alkaline Water Machine</h3>
    <div class="links"><span class="outline">See Why Are #1</span><span class="outline">Compare Water Ionizers</span></div>
  </div>
  <svg class="arrow" style="left:611px;top:172px" viewBox="0 0 28 56"><path d="M0 0l28 28L0 56z" fill="#fff"/><path d="M12 23l-5 5 5 5" fill="none" stroke="#2aa3de" stroke-width="2.5"/></svg>
  <svg class="arrow" style="left:1017px;top:172px" viewBox="0 0 28 56"><path d="M28 0L0 28l28 28z" fill="#fff"/><path d="M16 23l5 5-5 5" fill="none" stroke="#2aa3de" stroke-width="2.5"/></svg>
  <div class="quote">
    <div class="mark">&ldquo;</div>
    For the Quality of this water ionizer, I would have expected to pay double what i ended up paying for. Customer service was amazing.<br><br>Highly recommended!
    <div class="rule"></div>
    <div class="who">Maren &amp; Eli Vance,</div>
    <div class="where">Harlow Bay.</div>
  </div>
</section>

<section class="abs confidence">
  <h2>Shop with Confidence</h2>
  <div class="sub">Our Water Ionizers are Simply the Best!</div>
  <div class="pillars">
    <div class="pillar">
      <div class="ring"><svg width="30" height="30" viewBox="0 0 30 30"><path d="M3 13h5v14H3zM10 13l5-10c2 0 3 1.5 2.5 4L16 12h9c1.5 0 2.5 1.5 2 3l-3 10c-.4 1.3-1.4 2-2.7 2H10z" fill="#2aa3de"/></svg></div>
      <h4>Best Quality</h4>
      <p>We will ensure your Water Ionizer works<br>for life, guaranteed!</p>
    </div>
    <div class="pillar">
      <div class="ring fill"><span style="color:#fff;font-size:38px;font-weight:600">$</span></div>
      <h4>Money Back Guarantee</h4>
      <p>You have 90 days to test. we wont hassle<br>you, we swear!</p>
    </div>
    <div class="pillar">
      <div class="ring"><svg width="30" height="30" viewBox="0 0 30 30"><circle cx="15" cy="10" r="6" fill="#2aa3de"/><path d="M4 27c0-6 5-9 11-9s11 3 11 9z" fill="#2aa3de"/></svg></div>
      <h4>Customer Service</h4>
      <p>We will change the way you think about<br>customer service after buying from us!</p>
    </div>
  </div>
</section>

<section class="abs contact">
  <h2>Need Some Help Right Now?</h2>
  <div class="sub">Please fill out the form below with any questions you have. We will get back to you promptly.</div>
  <div class="form">
    <div class="row"><div class="field">Name</div><div class="field">Email</div><div class="field">Phone</div></div>
    <div class="field area">Type your Message ...</div>
    <div class="send">Send Message Now!</div>
  </div>
</section>

<footer class="abs footer">
  <div class="links">Home &nbsp;·&nbsp; Browse Products &nbsp;·&nbsp; <b>Why PureLumen?</b> &nbsp;·&nbsp; Compare &nbsp;·&nbsp; Support &nbsp;·&nbsp; FAQ &nbsp;·&nbsp; Testimonials</div>
  <div class="copy">© 2016 PureLumen All Rights Reserved. – Privacy Policy &amp; Terms &amp; Conditions</div>
  <div class="social"><span class="s1"></span><span class="s2"></span></div>
  <div class="up"><svg width="10" height="12" viewBox="0 0 10 12"><path d="M5 0L0 5h3v7h4V5h3z" fill="#fff"/></svg></div>
</footer>

</body>
</html>
```